Additional Benefits of Working for VALMIRA

Please prepare an infographic on the additional benefits besides salary of working at VALMIRA as detailed in the attached word document. Also attached is our logo in eps and our company design "Grounds". We are a Not For Profit company that finds jobs for unemployed people of government benefit payments

Brightstore Market(s)

Attracting people to work for VALMIRA. Making VALMIRA an employer of choice.

Font styles to use
Sans Serif

Colors

Designer to choose colors to be used in the design.

Requirements
Must have
• be on 1 page
• have our logo
Nice to have
• Our Grounds design worked into it.
• Happy engaged employees
• Community engagement - we are a not for profit organisation
Should not have
• Discrimination, swearing,

```html
<!DOCTYPE html>
<html lang="en">
<head>
<meta charset="utf-8">
<title>8 Benefits Working With VALMIRA</title>
<link rel="stylesheet" href="https://fonts.googleapis.com/css2?family=Poppins:wght@400;500;600;700&display=swap">
<style>
  :root {
    --page-bg: #ececec;
    --sheet: #ffffff;
    --ink: #1d1d1b;
    --teal: #2bbfae;
    --yellow: #f2c23a;
    --plum: #3a1f3d;
    --rose: #c2335c;
    --aqua: #79e0d6;
    --lavender: #a9a7ea;
    --lime: #5fdc5a;
    --olive: #b8d437;
    --red: #d3345a;
    --orange: #f4a12c;
    --flame: #f0502a;
    --navy: #3d4a6c;
    --slate: #6f7b98;
    --violet: #7a4fb6;
    --lilac: #b48be0;
    --ground-deep: #1f5d5a;
    --ground-green: #0d9b77;
  }
  * { box-sizing: border-box; margin: 0; padding: 0; }
  html, body { width: 1200px; height: 1200px; overflow: hidden; }
  body { background: var(--page-bg); font-family: "Poppins", sans-serif; color: var(--ink); }

  .sheet { position: absolute; left: 175px; top: 0; width: 850px; height: 1200px; background: var(--sheet); overflow: hidden; }
  .sheet-art { position: absolute; left: 0; top: 0; }

  .brand { position: absolute; left: 620px; top: 148px; display: flex; align-items: center; gap: 8px; }
  .brand-dot { width: 14px; height: 14px; border-radius: 50%; background: var(--lime); }
  .brand-name { font-weight: 700; font-size: 44px; letter-spacing: -1px; color: var(--ink); line-height: 1; }

  .heading { position: absolute; font-weight: 600; text-align: center; line-height: 1.05; transform: translateX(-50%); white-space: nowrap; }
  .heading.life { left: 425px; top: 296px; font-size: 15px; color: var(--teal); }
  .heading.diversity { left: 297px; top: 405px; font-size: 15.5px; color: var(--rose); line-height: 1.12; }
  .heading.wellbeing { left: 551px; top: 437px; font-size: 15px; color: var(--aqua); }
  .heading.career { left: 664px; top: 553px; font-size: 15px; color: var(--lime); line-height: 1.14; }
  .heading.recognition { left: 184px; top: 621px; font-size: 15px; color: var(--red); }
  .heading.community { left: 297px; top: 1015px; font-size: 15px; color: var(--orange); }
  .heading.perks { left: 425px; top: 1148px; font-size: 15px; color: var(--slate); }
  .heading.pay { left: 551px; top: 1015px; font-size: 15px; color: var(--lilac); line-height: 1.12; }

  .hub { position: absolute; left: 424px; top: 703px; transform: translateX(-50%); text-align: center; font-weight: 600; font-size: 19px; line-height: 1.12; color: var(--teal); white-space: nowrap; }

  .card-text { position: absolute; width: 64px; font-size: 5.3px; line-height: 1.25; color: var(--ink); }
  .card-text p { margin-bottom: 5px; }
  .card-text b { font-weight: 600; }
  .hl-teal { color: var(--teal); font-weight: 600; }
  .hl-rose { color: var(--rose); font-weight: 600; }
  .hl-lav { color: var(--lavender); font-weight: 600; }
  .hl-lime { color: var(--lime); font-weight: 600; }
  .hl-flame { color: var(--flame); font-weight: 600; }
  .hl-violet { color: var(--violet); font-weight: 600; }
  .hl-navy { color: #1f4e8c; font-weight: 600; }

  .text-life { left: 395px; top: 338px; }
  .text-diversity { left: 268px; top: 507px; }
  .text-wellbeing { left: 521px; top: 486px; }
  .text-career { left: 633px; top: 668px; }
  .text-recognition { left: 154px; top: 707px; }
  .text-community { left: 268px; top: 865px; }
  .text-perks { left: 395px; top: 979px; }
  .text-pay { left: 521px; top: 868px; }
</style>
</head>
<body>
<main class="sheet">
  <svg class="sheet-art" width="850" height="1200" viewBox="0 0 850 1200">
    <defs>
      <linearGradient id="groundsTone" x1="0" y1="0" x2="1" y2="1">
        <stop offset="0" stop-color="#0fa07c"/>
        <stop offset="0.45" stop-color="#1f6a66"/>
        <stop offset="0.75" stop-color="#4c6470"/>
        <stop offset="1" stop-color="#2f8f6a"/>
      </linearGradient>
      <linearGradient id="lifeStroke" x1="0" y1="0" x2="0" y2="1"><stop offset="0" stop-color="#f2c23a"/><stop offset="1" stop-color="#2bbfae"/></linearGradient>
      <linearGradient id="diversityStroke" x1="0" y1="0" x2="0" y2="1"><stop offset="0" stop-color="#c2335c"/><stop offset="1" stop-color="#3a1f3d"/></linearGradient>
      <linearGradient id="wellStroke" x1="0" y1="0" x2="0" y2="1"><stop offset="0" stop-color="#a9a7ea"/><stop offset="1" stop-color="#79e0d6"/></linearGradient>
      <linearGradient id="careerStroke" x1="0" y1="0" x2="0" y2="1"><stop offset="0" stop-color="#5fdc5a"/><stop offset="1" stop-color="#b8d437"/></linearGradient>
      <linearGradient id="recogStroke" x1="0" y1="0" x2="0" y2="1"><stop offset="0" stop-color="#c93b4a"/><stop offset="1" stop-color="#d3345a"/></linearGradient>
      <linearGradient id="commStroke" x1="0" y1="0" x2="0" y2="1"><stop offset="0" stop-color="#f4a12c"/><stop offset="1" stop-color="#f0502a"/></linearGradient>
      <linearGradient id="perksStroke" x1="0" y1="0" x2="0" y2="1"><stop offset="0" stop-color="#3d4a6c"/><stop offset="1" stop-color="#6f7b98"/></linearGradient>
      <linearGradient id="payStroke" x1="0" y1="0" x2="0" y2="1"><stop offset="0" stop-color="#7a4fb6"/><stop offset="1" stop-color="#b48be0"/></linearGradient>
    </defs>

    <polygon class="grounds-artwork" role="img" aria-label="VALMIRA Grounds artwork: dotted flowing lines and golden leaves in green and teal tones" points="0,0 687,0 0,526" fill="url(#groundsTone)"/>

    <g class="connectors" fill="none" stroke-width="2" stroke-linecap="round">
      <path d="M425 503 C470 600 530 700 512 760 C502 790 482 800 462 805" stroke="#b7c65a"/>
      <path d="M336 600 C420 615 490 640 500 705" stroke="#b8c878"/>
      <path d="M552 634 C540 700 520 780 462 810" stroke="#d4c34a"/>
      <path d="M627 736 C560 790 470 822 400 812" stroke="#e9c13e"/>
      <path d="M223 728 C300 680 380 640 449 654" stroke="#3bc2a6"/>
      <path d="M289 831 C300 750 340 690 400 661" stroke="#6cc98e"/>
      <path d="M436 961 C390 900 330 790 341 708" stroke="#8ccb7a"/>
      <path d="M513 865 C440 850 370 820 355 767" stroke="#9fc66c"/>
    </g>

    <g class="cards" fill="#fff" stroke-width="2">
      <rect x="387" y="327" width="76" height="176" rx="9" stroke="url(#lifeStroke)"/>
      <rect x="260" y="458" width="75" height="174" rx="9" stroke="url(#diversityStroke)"/>
      <rect x="513" y="458" width="76" height="174" rx="9" stroke="url(#wellStroke)"/>
      <rect x="625" y="644" width="75" height="175" rx="9" stroke="url(#careerStroke)"/>
      <rect x="146" y="644" width="75" height="175" rx="9" stroke="url(#recogStroke)"/>
      <rect x="260" y="832" width="75" height="174" rx="9" stroke="url(#commStroke)"/>
      <rect x="387" y="962" width="76" height="174" rx="9" stroke="url(#perksStroke)"/>
      <rect x="513" y="832" width="76" height="174" rx="9" stroke="url(#payStroke)"/>
    </g>
  </svg>

  <div class="brand"><span class="brand-name">valmira</span><span class="brand-dot"></span></div>

  <h2 class="heading life">Life Balance</h2>
  <h2 class="heading diversity">Diversity<br>&amp;<br>Inclusion</h2>
  <h2 class="heading wellbeing">Wellbeing</h2>
  <h2 class="heading career">Career<br>Growth<br>&amp;<br>Professional<br>Development</h2>
  <h2 class="heading recognition">Recognition</h2>
  <h2 class="heading community">Contributing<br>to Community</h2>
  <h2 class="heading perks">Benefits</h2>
  <h2 class="heading pay">Remuneration<br>&amp;<br>Salary Packaging</h2>

  <h1 class="hub">8 Benefits<br>Working<br>With US</h1>

  <div class="card-text text-life">
    <p class="hl-teal">VALMIRA Day Leave</p>
    <p>An extra day off at Christmas!</p>
    <p>Birthday Leave. A paid day off on your birthday</p>
    <p>A day off every month as Time in Lieu</p>
    <p><span class="hl-teal">4 weeks</span> Annual Leave</p>
    <p>Generous Personal Leave</p>
    <p>Support for parental leave for the birth or adoption of a child</p>
    <p><span class="hl-teal">Flexible</span> work arrangements</p>
  </div>

  <div class="card-text text-diversity">
    <p>An inclusive and <span class="hl-rose">diverse</span> culture where different backgrounds, experiences and perspectives are <span class="hl-rose">valued</span></p>
    <p>Gender diversity. Over <span class="hl-rose">50%</span> of our workforce and our leaders are <span class="hl-rose">female.</span></p>
  </div>

  <div class="card-text text-wellbeing">
    <p>Up to <span class="hl-lav">$450</span> per year to spend on Wellbeing services such as gym or yoga memberships</p>
    <p><span class="hl-lav">Free</span> counselling services <span class="hl-lav">24x7</span> via our Employee Assistance Program</p>
    <p>Discount private health insurance</p>
    <p>WHS policies which support a safe, inclusive work place</p>
  </div>

  <div class="card-text text-career">
    <p>Ongoing internal training and development opportunities.</p>
    <p>External study support &amp; study leave</p>
    <p>Access to the tools and technology to do your job well</p>
    <p><span class="hl-lime">Career advancement</span> opportunities</p>
    <p>Internal job vacancy listings</p>
  </div>

  <div class="card-text text-recognition">
    <p>We <span class="hl-rose">celebrate</span> our people for reaching service milestones</p>
    <p>Team &amp; individual recognition for high performance</p>
  </div>

  <div class="card-text text-community">
    <p>Team involvement in local charity and community events</p>
    <p>Participation in VALMIRA's <span class="hl-flame">1000 Jobs</span> in 100 days initiative</p>
    <p>Strong relationships and connection with Indigenous Communities in support of Indigenous Employment</p>
  </div>

  <div class="card-text text-perks">
    <p>Discounted vouchers for: <span class="hl-navy">Harvest Mart, Greenleaf Grocers, Voltline, Starview Cinemas, Cellar Row, ValueWay, Brightstore, Campfield</span> and many others via Paywise e-wallet</p>
    <p>A range of other employee discounts are also available, including access to discounted banking and finance, vehicle purchasing, leasing and hotel accommodation</p>
  </div>

  <div class="card-text text-pay">
    <p>Competitive salary</p>
    <p>Ability to salary package up to <span class="hl-violet">$15,900</span> and reduce your tax. Package rent, home loans, child care and much more</p>
    <p>Salary package up to <span class="hl-violet">$2,650</span> on meal entertainment and holiday accommodation</p>
  </div>
</main>
</body>
</html>
```